Tidewell Giving Fund - New Website Designed

I need a site that looks like this http://www.ridgelanegiving.org for boat donations. So please replace the cars with boats.

```html
<!DOCTYPE html>
<html lang="en">
<head>
<meta charset="utf-8">
<title>Tidewell Giving Fund – Donate Your Boat</title>
<link rel="stylesheet" href="https://fonts.googleapis.com/css2?family=Archivo:wght@400;600;700;800;900&family=Roboto:wght@400;500&display=swap">
<style>
:root{
  --red:#c0111a;
  --red-dark:#a50c14;
  --navy:#101d6b;
  --blue:#1a32a8;
  --nav-blue:#1f36a6;
  --grey:#cfcfcf;
  --grey-light:#ebebeb;
  --form-grey:#bdbdbd;
  --text:#222;
  --muted:#444;
  --white:#fff;
}
*{box-sizing:border-box;margin:0;padding:0}
html,body{width:1200px;height:1200px;overflow:hidden;background:var(--grey-light);font-family:"Archivo",Arial,sans-serif;color:var(--text)}
.canvas{position:relative;width:1200px;height:1200px;background:var(--grey-light)}
.abs{position:absolute}

/* header */
.header{left:105px;top:5px;width:989px;height:107px;background:linear-gradient(100deg,#151c3c 0%,#2a2f55 40%,#7d1520 70%,#9c1a22 100%)}
.brand{left:150px;top:44px;display:flex;align-items:center;gap:10px}
.brand-mark{width:18px;height:18px;border-radius:50%;background:var(--red)}
.brand-name{font-weight:800;font-size:24px;color:#e9b84a;letter-spacing:.5px;text-transform:uppercase}
.nav{left:105px;top:112px;width:670px;height:30px;background:var(--nav-blue);display:flex;align-items:center;padding-left:139px;gap:22px}
.nav a{color:var(--white);font-weight:800;font-size:12.5px;text-decoration:none;letter-spacing:.2px}
.nav-strip{left:1062px;top:112px;width:32px;height:30px;background:var(--nav-blue)}
.hero{left:105px;top:142px;width:668px;height:278px;background:linear-gradient(180deg,#8fb7e2 0%,#b7d2ec 45%,#6d8aa6 62%,#8d8470 80%,#b7a27c 100%)}
.hero-edge{left:1062px;top:142px;width:32px;height:278px;background:linear-gradient(180deg,#a7c5e6,#6d8aa6)}

/* donate panel */
.panel{left:773px;top:5px;width:289px;height:415px;background:var(--red)}
.call{left:788px;top:33px;display:flex;align-items:center;gap:12px}
.call-text{color:var(--white);text-align:center}
.call-text .t1{font-weight:800;font-size:13.5px}
.call-text .t2{font-weight:900;font-size:20px;letter-spacing:1.5px;line-height:1.2}
.call-text .t3{font-weight:600;font-size:7.5px}
.panel-tab{left:766px;top:103px;width:303px;height:32px;background:var(--white);color:var(--red);font-weight:800;font-size:14px;display:flex;align-items:center;justify-content:center}
.panel-notch{left:903px;top:90px;width:28px;height:16px;border-radius:50%;background:var(--red);border:2px solid var(--white)}
.panel-sub{left:773px;top:144px;width:289px;text-align:center;color:var(--white);font-weight:700;font-size:12px}
.form{left:789px;top:167px;width:256px;height:269px;background:var(--form-grey);border:1px solid #999;padding:27px 13px 0 13px}
.field{width:230px;height:18px;background:var(--white);border:1px solid #ddd;margin-bottom:8.3px;font-family:"Roboto",Arial,sans-serif;font-size:7.5px;color:#999;padding:4px 8px}
.btn{display:inline-block;margin-top:2px;background:var(--blue);color:var(--white);font-size:8px;font-weight:600;padding:6px 12px;border:1px solid #0c1e7a}

/* benefits band */
.band{left:94px;top:458px;width:1002px;height:142px;background:var(--grey)}
.band-fold-l{left:94px;top:463px}
.banner{left:126px;top:458px;width:328px;height:142px;background:linear-gradient(120deg,#17279a,#2b46c7 60%,#1c2f9e);display:flex;flex-direction:column;justify-content:center;padding-left:32px;color:var(--white)}
.banner .b1,.banner .b3{font-weight:800;font-size:19px}
.banner .b2{font-weight:900;font-size:38px;color:#e3b23c;letter-spacing:2px;line-height:1.05}
.perks{left:470px;top:484px;display:flex}
.perk{width:130px;text-align:center;color:var(--red);font-family:"Roboto",Arial,sans-serif;font-size:12.5px;line-height:1.2}
.perk:first-child{width:86px}
.perk svg{display:block;margin:0 auto 10px;height:40px}

/* how */
.how{left:94px;top:600px;width:1002px;height:74px;background:var(--white)}
.sec-title{font-weight:900;font-size:21px;text-align:center;display:flex;align-items:center;justify-content:center;gap:22px}
.sec-title i{display:block;width:108px;height:1px;background:#999}
.sec-title .blue{color:var(--navy)}
.sec-title .red{color:var(--red)}
.how-title{left:94px;top:636px;width:1002px}
.rule{left:80px;top:673px;width:1040px;height:1px;background:#ccc}
.steps{left:100px;top:677px;width:996px;height:159px;background:var(--white)}
.step{top:700px;display:flex;gap:16px}
.step h3{font-weight:800;font-size:11px;color:var(--navy);margin-top:26px;line-height:1.2}
.step p{font-family:"Roboto",Arial,sans-serif;font-size:8.8px;color:var(--muted);line-height:1.25;margin-top:10px}

/* why */
.why{left:100px;top:836px;width:996px;height:308px;background:linear-gradient(180deg,#d9d4cc 0%,#ead9c2 35%,#d8c2a6 70%,#8e7c68 100%)}
.why-title{left:100px;top:884px;width:996px}
.why-list{left:195px;top:938px;list-style:none}
.why-list li{display:flex;align-items:center;gap:10px;font-size:10.3px;height:23.7px;color:#111}
.why-list b{font-weight:800}
.arrow{width:16px;height:16px;border-radius:50%;background:var(--red);display:flex;align-items:center;justify-content:center;flex:none}

/* footer */
.footer{left:80px;top:1164px;width:1040px;height:33px;background:var(--white);border-bottom:2px solid #555;font-family:"Roboto",Arial,sans-serif;font-size:8px;color:#555;text-align:center;padding-top:13px}
</style>
</head>
<body>
<div class="canvas">

  <header>
    <div class="abs header" role="img" aria-label="Waving American flag background"></div>
    <div class="abs brand"><span class="brand-mark"></span><span class="brand-name">Tidewell Giving Fund</span></div>
    <nav class="abs nav"><a href="#">HOW TO DONATE</a><a href="#">WHY DONATE</a><a href="#">FAQ</a><a href="#">ABOUT</a></nav>
    <div class="abs nav-strip"></div>
  </header>

  <div class="abs hero" role="img" aria-label="Soldier embracing his daughter holding a small flag beside a white center-console boat on the water"></div>
  <div class="abs hero-edge" role="img" aria-label="Water and jet ski"></div>

  <aside>
    <div class="abs panel"></div>
    <div class="abs call">
      <svg width="54" height="54" viewBox="0 0 54 54"><circle cx="27" cy="27" r="24" fill="none" stroke="#fff" stroke-width="3.5"/><path d="M19 15c2-1 4 0 5 2l2 5c0 2-1 3-2 4 1 3 4 6 7 7 1-1 2-2 4-2l5 2c2 1 3 3 2 5-2 3-5 4-8 3-8-3-14-9-17-17-1-3 0-6 2-9z" fill="#fff"/></svg>
      <div class="call-text"><div class="t1">CALL TODAY TO DONATE</div><div class="t2">1-800-555-0142</div><div class="t3">Live Operators Available - 7 Days A Week</div></div>
    </div>
    <div class="abs panel-notch"></div>
    <div class="abs panel-tab">DONATE YOUR BOAT ONLINE</div>
    <div class="abs panel-sub">Full Tax Deduction - Running or Not</div>
    <form class="abs form">
      <div class="field">First Name</div>
      <div class="field">Last Name</div>
      <div class="field">Daytime Phone</div>
      <div class="field">Email</div>
      <div class="field">Zip Code</div>
      <div class="field">Chose Year</div>
      <div class="field">BOAT Model</div>
      <span class="btn">DONATE NOW!</span>
    </form>
  </aside>

  <section>
    <div class="abs band"></div>
    <svg class="abs" style="left:94px;top:463px" width="34" height="132"><polygon points="0,0 34,0 34,132 0,132 28,66" fill="#000"/></svg>
    <svg class="abs" style="left:454px;top:463px" width="30" height="132"><polygon points="0,0 30,0 0,66 30,132 0,132" fill="#000"/></svg>
    <div class="abs banner"><div class="b1">DONATE YOUR BOAT TO</div><div class="b2">VETERANS</div><div class="b3">MAKE A DIFFERENCE</div></div>
    <div class="abs perks">
      <div class="perk"><svg viewBox="0 0 48 48" width="48"><circle cx="22" cy="26" r="18" fill="none" stroke="#1a32a8" stroke-width="4"/><path d="M13 25l8 8 20-22" fill="none" stroke="#1a32a8" stroke-width="5"/></svg>You have<br>no costs</div>
      <div class="perk"><svg viewBox="0 0 60 48" width="60"><path d="M6 30l10-22 6 3-8 19z" fill="#1a32a8"/><rect x="24" y="16" width="32" height="16" rx="3" fill="#1a32a8"/><circle cx="14" cy="38" r="6" fill="none" stroke="#1a32a8" stroke-width="3"/><circle cx="46" cy="38" r="6" fill="none" stroke="#1a32a8" stroke-width="3"/></svg>Free towing,<br>running or not</div>
      <div class="perk"><svg viewBox="0 0 40 48" width="40"><rect x="4" y="2" width="32" height="42" fill="none" stroke="#1a32a8" stroke-width="3"/><path d="M10 12h20M10 18h20M10 32h20" stroke="#1a32a8" stroke-width="2"/><text x="11" y="29" font-size="11" font-weight="700" fill="#1a32a8" font-family="Arial">$≡</text></svg>We issue you an<br>IRS tax receipt</div>
      <div class="perk"><svg viewBox="0 0 52 48" width="52"><rect x="18" y="4" width="30" height="36" fill="none" stroke="#1a32a8" stroke-width="3"/><path d="M32 14h12M32 20h12M32 26h12" stroke="#1a32a8" stroke-width="2"/><circle cx="20" cy="24" r="9" fill="#fff" stroke="#1a32a8" stroke-width="3"/><path d="M13 31l-9 9" stroke="#1a32a8" stroke-width="4"/></svg>We take care of<br>all paperwork</div>
      <div class="perk" style="width:170px"><svg viewBox="0 0 40 48" width="40"><rect x="4" y="6" width="32" height="40" fill="none" stroke="#1a32a8" stroke-width="3"/><rect x="13" y="2" width="14" height="8" fill="#1a32a8"/><path d="M10 20h20M10 26h20M10 32h20M10 38h14" stroke="#1a32a8" stroke-width="2"/></svg>We take care of<br>DMV &amp; Smog issues</div>
    </div>
  </section>

  <section>
    <div class="abs how"></div>
    <h2 class="abs sec-title how-title"><i></i><span><span class="blue">HOW TO </span><span class="red">DONATE</span></span><i></i></h2>
    <div class="abs rule"></div>
    <div class="abs steps"></div>
    <div class="abs step" style="left:135px">
      <svg width="70" height="70" viewBox="0 0 70 70"><rect x="16" y="5" width="10" height="7" fill="#c0111a"/><rect x="31" y="5" width="34" height="7" fill="#c0111a"/><rect x="16" y="18" width="10" height="7" fill="#c0111a"/><rect x="31" y="18" width="34" height="7" fill="#c0111a"/><rect x="31" y="31" width="26" height="7" fill="#c0111a"/><path d="M22 36l-10 14 5 1-6 14 5-1 6-14 5 1z" fill="#c0111a"/><path d="M36 66l44-44" stroke="#ddd"/></svg>
      <div><h3>CALL US AT 1-800-555-0142 OR<br>FILL OUT THE ONLINE FORM</h3><p>Donating your Boat is easy and<br>donation is accepted nationwide.</p></div>
    </div>
    <div class="abs step" style="left:475px">
      <svg width="80" height="60" viewBox="0 0 80 60"><path d="M2 10h26v26H2z" fill="#c0111a"/><path d="M28 10l16 12" stroke="#c0111a" stroke-width="4"/><rect x="42" y="18" width="34" height="14" rx="6" fill="#c0111a"/><circle cx="14" cy="40" r="7" fill="#fff" stroke="#c0111a" stroke-width="4"/><circle cx="56" cy="32" r="6" fill="#fff" stroke="#c0111a" stroke-width="4"/></svg>
      <div style="margin-left:-6px"><h3 style="margin-left:20px">WE TOW THE BOAT</h3><p>Any Boat is accepted and we will<br>arrange to pick up your Boat when<br>it is most convenient for you.</p></div>
    </div>
    <div class="abs step" style="left:780px">
      <svg width="60" height="62" viewBox="0 0 60 62"><rect x="10" y="2" width="44" height="50" fill="none" stroke="#c0111a" stroke-width="3"/><rect x="2" y="8" width="44" height="50" fill="#fff" stroke="#c0111a" stroke-width="3"/><text x="16" y="30" font-size="16" font-weight="800" fill="#c0111a" font-family="Arial">$</text><path d="M10 38h28M10 44h28M10 50h28M18 34v20M28 34v20" stroke="#c0111a" stroke-width="2"/></svg>
      <div><h3 style="margin-left:10px">TAX WRITE-OFF</h3><p>Once the Boat donation is<br>complete, you will receive your<br>tax deductable vehicle donation<br>receipt.</p></div>
    </div>
  </section>

  <section>
    <div class="abs why" role="img" aria-label="Soldiers raising a large American flag at sunset"></div>
    <h2 class="abs sec-title why-title"><i></i><span><span class="blue">WHY DONATE </span><span class="red">YOUR BOAT TO US</span></span><i></i></h2>
    <ul class="abs why-list">
      <li><span class="arrow"><svg width="10" height="10" viewBox="0 0 10 10"><path d="M1 5h7M5 2l3 3-3 3" stroke="#fff" stroke-width="1.6" fill="none"/></svg></span><span><b>Top Rated &amp; IRS 501(c)3 Approved :</b> Free 24/7 Pickup with No DMV Hassles.</span></li>
      <li><span class="arrow"><svg width="10" height="10" viewBox="0 0 10 10"><path d="M1 5h7M5 2l3 3-3 3" stroke="#fff" stroke-width="1.6" fill="none"/></svg></span><span><b>Free Local Towing :</b> We will pick up your Boat donation, running or not, when it's most convenient, at home or work.</span></li>
      <li><span class="arrow"><svg width="10" height="10" viewBox="0 0 10 10"><path d="M1 5h7M5 2l3 3-3 3" stroke="#fff" stroke-width="1.6" fill="none"/></svg></span><span><b>All Boats Accepted :</b> We take your car regardless of its condition or registration status.</span></li>
      <li><span class="arrow"><svg width="10" height="10" viewBox="0 0 10 10"><path d="M1 5h7M5 2l3 3-3 3" stroke="#fff" stroke-width="1.6" fill="none"/></svg></span><span><b>Income Tax Deduction :</b> We issue you an IRS tax receipt &amp; offer the largest resale network to get you the highest tax write-off possible.</span></li>
      <li><span class="arrow"><svg width="10" height="10" viewBox="0 0 10 10"><path d="M1 5h7M5 2l3 3-3 3" stroke="#fff" stroke-width="1.6" fill="none"/></svg></span><span><b>No Paperwork Hassles :</b> We take any Boat and handle everything: DMV, Smog and IRS paperwork.</span></li>
      <li><span class="arrow"><svg width="10" height="10" viewBox="0 0 10 10"><path d="M1 5h7M5 2l3 3-3 3" stroke="#fff" stroke-width="1.6" fill="none"/></svg></span><span><b>Boat donations help fund programs :</b> And benefit Harbor Service Relief Fund. An IRS 501(c)3 nonprofit organization.</span></li>
      <li><span class="arrow"><svg width="10" height="10" viewBox="0 0 10 10"><path d="M1 5h7M5 2l3 3-3 3" stroke="#fff" stroke-width="1.6" fill="none"/></svg></span><span><b>Schedule a Free Pickup :</b> Complete the form and a representative will call you to arrange a convenient time to pickup your Boat.</span></li>
    </ul>
  </section>

  <footer class="abs footer">CopyRight © 2017 Tidewell Giving Fund.</footer>
</div>
</body>
</html>
```